Solo Law Practice Website Design

I am starting a solo law practice that will specialize in criminal defense and family law.

I have a rudimentary understanding of Wordpress as used through the tidalnest web services. The winning design would be compatible with this system so that I can modify content on my own.

I have supplied the written content and the components that I am looking for at the domain name: morganvaleslaw.com.

I would like to take that content and work it into a website that looks more professional and inviting. The two most important goals of the website are ease of navigation and rich content for search engine spiders (for example, integrating articles into pages rather than linking to a word document).

The winning design should be turnkey for me to upload immediately.
Updates

Reason: I will be traveling.

Target Market(s)

Individuals looking for legal services.

Industry/Entity Type

Defense

Requirements
Must have
• My picture should appear at least once in the site.

The design should allow a space for me to post blog or legal updates. Additionally, there should be functionality for me to add additional articles to the site.
Nice to have
• Appropriate pictures for a legal website to break-up text on pages.

Simple flash features that won't significantly slow loading times.

Widgets that drive traffic to a contact page or function.

```html
<!DOCTYPE html>
<html lang="en">
<head>
<meta charset="utf-8">
<title>Law Offices of Morgan Vales PLLC</title>
<link rel="stylesheet" href="https://fonts.googleapis.com/css2?family=Arimo:wght@400;700&display=swap">
<style>
:root{
  --parchment:#efd6a2;
  --parchment-light:#f6e4bd;
  --parchment-dark:#e6bd74;
  --maroon:#7a1f2e;
  --brown:#3b2818;
  --ink:#222;
  --muted:#666;
  --rule:#8a8070;
  --field:#ececec;
  --field-line:#b9b9b9;
  --green:#1c9b3b;
  --link:#2a6bb8;
}
*{box-sizing:border-box;margin:0;padding:0}
html,body{width:1121px;height:1200px;overflow:hidden;background:#fff}
body{font-family:"Arimo",Arial,sans-serif;color:var(--ink)}
.page{position:relative;width:1028px;height:1100px;transform:scale(1.0905);transform-origin:0 0}
.abs{position:absolute}
.masthead{left:0;top:0;width:1028px;height:496px;background:radial-gradient(ellipse at 40% 30%,var(--parchment-light),var(--parchment) 60%,#e7c88e)}
.brand-mark{left:27px;top:24px;width:56px;height:56px;border-radius:50%;background:var(--brown);border:3px solid #b08850}
.brand-name{left:100px;top:33px;font-size:21px;font-weight:700;color:var(--maroon);white-space:nowrap}
.brand-tag{left:100px;top:56px;font-size:14px;color:#555}
.search{left:757px;top:40px;width:247px;height:26px;background:#f1f1f1;border:1px solid #bbb}
.search svg{position:absolute;right:8px;top:4px}
.rule{height:1px;background:var(--rule)}
.nav{left:26px;top:102px;display:flex;align-items:center;font-size:14.5px;color:#2a2a2a}
.nav a{color:inherit;text-decoration:none;padding:0 6px;border-right:2px dotted #6b5a44;line-height:18px}
.nav a:last-child{border-right:0}
.nav .current{background:var(--brown);color:#fff;border:1px solid #c9a46a;padding:6px 13px;line-height:16px;margin-right:2px;border-right:1px solid #c9a46a}
.hero-mark{left:110px;top:180px;width:168px;height:168px;border-radius:50%;background:var(--brown);border:4px solid #b08850}
.hero-line{left:35px;font-weight:400;color:#2a2a2a;white-space:nowrap}
.portrait-frame{left:393px;top:160px;width:609px;height:312px;background:#fff;padding:5px;box-shadow:0 1px 4px rgba(0,0,0,.3)}
.portrait{width:100%;height:100%;background:radial-gradient(ellipse at 50% 55%,#c89a88 0%,#8c4a30 45%,#4a1c10 100%)}
.lead-heading{left:24px;top:522px;font-size:27px;color:var(--maroon);font-weight:400}
.intro{left:26px;top:574px;width:612px;font-size:13px;line-height:16px}
.intro .sub{font-size:14px;font-weight:700;margin-bottom:10px}
.intro h3{font-size:13px;font-weight:700}
.intro p{margin-bottom:16px}
.read-more{left:567px;top:916px;font-size:11px;color:var(--muted);letter-spacing:.3px}
.call-box{left:695px;top:525px;width:309px;height:92px;border-top:1px solid #ccc;border-bottom:1px solid #ccc}
.call-icon{position:absolute;left:18px;top:9px;width:94px;height:73px;background:#f4f4f4}
.call-title{position:absolute;left:150px;top:14px;font-size:22px;color:var(--green)}
.call-note{position:absolute;left:153px;top:42px;font-size:9px;color:#888;line-height:12px}
.call-by{position:absolute;left:210px;top:69px;font-size:10px;color:#666}
.form-title{left:697px;top:642px;font-size:26px;color:var(--maroon)}
.field{left:701px;width:269px;height:27px;background:var(--field);border:1px solid var(--field-line);font-size:11px;color:#666;padding:7px 10px}
.field.area{height:70px}
.submit{left:714px;top:907px;width:94px;height:30px;border:1px solid #aaa;background:linear-gradient(#fafafa,#dedede);font-size:11px;text-align:center;line-height:28px;letter-spacing:.5px}
.footer{left:0;top:972px;width:1028px;height:128px;background:radial-gradient(ellipse at 30% 40%,var(--parchment-light),var(--parchment) 70%)}
.foot-links{left:26px;top:990px;font-size:11px;color:#333}
.foot-legal{left:33px;top:1038px;font-size:11px;color:#555;line-height:18px}
.foot-legal .copy{margin-left:-4px}
.share{top:1047px;height:19px;font-size:11px;font-weight:700;display:flex;align-items:center;padding:0 8px}
.share-a{left:370px;width:60px;background:#4a64a0;color:#fff}
.share-b{left:441px;width:58px;background:#eef2f6;border:1px solid #aab;color:#333}
.count{left:503px;top:1047px;width:15px;height:19px;background:#fff;border:1px solid #bbb;font-size:10px;text-align:center;line-height:17px}
.util{top:1046px;font-size:14px;color:var(--link);display:flex;align-items:center;gap:5px}
.subscribe{left:738px;top:972px;width:266px;height:110px;background:var(--parchment-dark)}
.subscribe h4{position:absolute;left:10px;top:13px;font-size:15px;font-weight:400;color:#222}
.subscribe p{position:absolute;left:11px;top:39px;width:240px;font-size:10px;line-height:14px;color:#222}
.subscribe .input{position:absolute;left:9px;top:74px;width:214px;height:26px;background:#f4f4f4;border:1px solid #aaa}
.subscribe .go{position:absolute;left:226px;top:74px;width:31px;height:26px;background:#eee;border:1px solid #aaa;font-size:12px;text-align:center;line-height:24px}
</style>
</head>
<body>
<div class="page">
  <header class="abs masthead"></header>
  <div class="abs brand-mark"></div>
  <div class="abs brand-name">Law Offices of Morgan Vales PLLC</div>
  <div class="abs brand-tag">Affordable Legal Representation</div>
  <div class="abs search">
    <svg width="16" height="16" viewBox="0 0 16 16"><circle cx="6.5" cy="6.5" r="5" fill="none" stroke="#7a1f2e" stroke-width="2"/><line x1="10" y1="10" x2="14.5" y2="14.5" stroke="#7a1f2e" stroke-width="2.4"/></svg>
  </div>
  <div class="abs rule" style="left:24px;top:94px;width:980px"></div>
  <nav class="abs nav">
    <a class="current">Home</a><a>Contact Me</a><a>Criminal Law</a><a>Family Law</a><a>Will Drafting</a><a>Attorney Profile</a><a>Fees</a><a>Legal Updates</a><a>Online Resources</a><a>Articles</a>
  </nav>
  <div class="abs rule" style="left:24px;top:139px;width:980px"></div>
  <div class="abs hero-mark"></div>
  <div class="abs hero-line" style="top:386px;font-size:31px">AFFORDABLE LEGAL</div>
  <div class="abs hero-line" style="top:418px;font-size:36px">REPRESENTATION</div>
  <div class="abs portrait-frame"><div class="portrait" role="img" aria-label="Portrait photograph of the attorney in a white shirt and tie"></div></div>

  <h1 class="abs lead-heading">Specializing in Criminal Defense and Family Law</h1>
  <section class="abs intro">
    <div class="sub">Delivering legal services in the greater Twin Cities area.</div>
    <h3>About Me.</h3>
    <p>My practice is focused on accomplishing your goals through results-oriented work at a discount price. For your convenience, I handle legal matters throughout the Twin Cities, including Hennepin, Ramsey, Anoka, and Washington counties.&nbsp; I understand that legal issues can appear complicated, and that is why I take a hands-on approach to guiding you through your legal needs.</p>
    <h3>Personal Attention.</h3>
    <p>I control the size of my practice so that I am able to devote 100% of my effort to each case.&nbsp; I have no “associates” so I handle every case personally.</p>
    <h3>General Practice.</h3>
    <p>I am available to provide your defense if you are accused of a felony or misdemeanor.&nbsp; Additionally, I can work with you on family matters such as divorce, child custody, wills, and nuptial agreements.</p>
    <h3>In our first consultation,</h3>
    <p>I will take time to listen to your individual situation.&nbsp;&nbsp; I will explain the legal issues, and the risks involved in each course of action we may pursue so that you can make informed decisions about how to proceed.</p>
  </section>
  <div class="abs read-more">READ MORE</div>

  <aside class="abs call-box">
    <div class="call-icon">
      <svg width="94" height="73" viewBox="0 0 94 73"><ellipse cx="48" cy="34" rx="42" ry="29" fill="#fff" stroke="#555" stroke-width="3"/><path d="M22 62 L30 52 L36 58 Z" fill="#555"/><path d="M36 18 c-5 3 -6 10 2 20 c8 10 16 13 21 9 l3-3 -7-7 -4 3 c-4-2-8-7-10-11 l3-4 -6-8 z" fill="#1d4f9a"/></svg>
    </div>
    <div class="call-title">Call Me</div>
    <div class="call-note">Click and Dialwise will<br>connect you for free.</div>
    <div class="call-by">by Dialwise</div>
  </aside>
  <h2 class="abs form-title" style="font-weight:400">Quick Contact</h2>
  <div class="abs field" style="top:682px">Name(required)</div>
  <div class="abs field" style="top:718px">Email</div>
  <div class="abs field" style="top:754px">Phone</div>
  <div class="abs field" style="top:790px">Preferred Contact Method
    <svg style="position:absolute;right:8px;top:9px" width="11" height="9" viewBox="0 0 11 9"><path d="M0 0h11L5.5 9z" fill="#555"/></svg>
  </div>
  <div class="abs field area" style="top:827px">Please briefly describe your legal issue(required)</div>
  <div class="abs submit">SUBMIT</div>

  <footer class="abs footer"></footer>
  <div class="abs foot-links">Home | Contact Me | Criminal Law | Family Law | Will Drafting | Attorney Profile | Fees | Legal Updates | Online Resources | Articles</div>
  <div class="abs foot-legal">Terms of Service - Privacy Policy - Program Policies<br><span class="copy">© 2012 Law Offices of Morgan Vales PLLC</span></div>
  <div class="abs share share-a">Share</div>
  <div class="abs share share-b">Post</div>
  <div class="abs count">0</div>
  <div class="abs util" style="left:548px">
    <svg width="13" height="10" viewBox="0 0 13 10"><rect x=".5" y=".5" width="12" height="9" fill="#fff" stroke="#2a6bb8"/><path d="M.5 .5l6 5 6-5" fill="none" stroke="#2a6bb8"/></svg>Email
  </div>
  <div class="abs util" style="left:612px">
    <svg width="14" height="13" viewBox="0 0 14 13"><rect x="3" y="0" width="8" height="4" fill="#fff" stroke="#555"/><rect x=".5" y="4" width="13" height="6" fill="#8aa3c4" stroke="#555"/><rect x="3" y="8" width="8" height="5" fill="#fff" stroke="#555"/></svg>Print
  </div>
  <div class="abs subscribe">
    <h4>Subscribe to receive legal updates</h4>
    <p>Enter your email address to receive notifications of legal updates by e-mail</p>
    <div class="input"></div>
    <div class="go">Go</div>
  </div>
</div>
</body>
</html>
```